Meridian Rest Supply Needs Business Card

Looking for a very nice looking business card. Creative but not extravagant. We sell beds and pillows across the U.S. and need something professional but catchy. I have attached the logo.

Name : Dale Fenwick
Title : President
Phone : (800) 417-2964
Email: sleep@quorvana.com
Website: www.quorvana.com

Can be single-sided or double-sided
horizontal or vertical

Can use Blues/Greys

Target Market(s)

Mass Market

Industry/Entity Type

Retail

Contact Information for Business Card

Name : Dale Fenwick
Title : President
Phone : (800) 417-2964
Email: sleep@quorvana.com
Website: www.quorvana.com

Requirements
Must have
• Clean, Modern, Smooth
• Can use Blues/Greys
• On the other side without the information - have something simple like www.quorvana.com or our logo
Nice to have
• Surprise me
Should not have
• Nothing crazy, nothing cluttered

```html
<!DOCTYPE html>
<html lang="en">
<head>
<meta charset="utf-8">
<title>Meridian Rest Supply — Business Card</title>
<link href="https://fonts.googleapis.com/css2?family=Roboto:wght@300;400;500;700&display=swap" rel="stylesheet">
<style>
  :root {
    --page-bg: #dfe6ee;
    --card-bg: #f3f6f9;
    --card-edge: #c9d2dc;
    --rule: #8d97a3;
    --brand-blue: #2b79bb;
    --name-blue: #2f6fae;
    --text-grey: #4a4f57;
    --icon-blue: #3b6f9f;
  }
  * { margin: 0; padding: 0; box-sizing: border-box; }
  html, body {
    width: 1200px;
    height: 900px;
    overflow: hidden;
    background: var(--page-bg);
    font-family: "Roboto", Arial, sans-serif;
  }
  .card {
    position: absolute;
    left: 225px;
    top: 237px;
    width: 750px;
    height: 427px;
    background: var(--card-bg);
    border: 1px solid var(--card-edge);
    box-shadow: 0 10px 30px rgba(40, 60, 90, 0.12);
  }
  .card__rule {
    position: absolute;
    left: 74px;
    top: 0;
    bottom: 0;
    width: 1px;
    background: var(--rule);
  }
  .brand-name {
    position: absolute;
    right: 33px;
    top: 18px;
    font-family: "Roboto", Arial, sans-serif;
    font-weight: 300;
    font-size: 66px;
    letter-spacing: 1px;
    color: var(--brand-blue);
    line-height: 1.3;
  }
  .holder {
    position: absolute;
    left: 99px;
    top: 212px;
  }
  .holder__name {
    font-weight: 700;
    font-size: 19px;
    letter-spacing: 0.5px;
    color: var(--name-blue);
    line-height: 24px;
  }
  .holder__title {
    font-weight: 500;
    font-size: 17px;
    color: var(--text-grey);
    line-height: 22px;
    margin-top: 0;
  }
  .contact-list {
    position: absolute;
    left: 63px;
    top: 279px;
    list-style: none;
  }
  .contact-list__item {
    display: flex;
    align-items: center;
    height: 27px;
    font-size: 17px;
    color: var(--text-grey);
  }
  .contact-list__icon {
    width: 22px;
    height: 22px;
    margin-right: 14px;
    flex: none;
  }
</style>
</head>
<body>
  <main class="card">
    <div class="card__rule"></div>
    <div class="brand-name">quorvana</div>

    <div class="holder">
      <div class="holder__name">DALE FENWICK</div>
      <div class="holder__title">President</div>
    </div>

    <ul class="contact-list">
      <li class="contact-list__item">
        <svg class="contact-list__icon" viewBox="0 0 22 22" aria-hidden="true">
          <circle cx="11" cy="11" r="10" fill="var(--icon-blue)"/>
          <path d="M7.6 6.2l1.7-.4 1.2 2.6-1.1.9a6 6 0 0 0 3.3 3.3l.9-1.1 2.6 1.2-.4 1.7c-.2.5-.7.8-1.3.7A8.6 8.6 0 0 1 6.9 7.5c-.1-.6.2-1.1.7-1.3z" fill="#fff"/>
        </svg>
        (800) 417-2964
      </li>
      <li class="contact-list__item">
        <svg class="contact-list__icon" viewBox="0 0 22 22" aria-hidden="true">
          <circle cx="11" cy="11" r="10" fill="var(--icon-blue)"/>
          <rect x="6" y="7.5" width="10" height="7" rx="0.8" fill="#fff"/>
          <path d="M6.3 8l4.7 3.6L15.7 8" fill="none" stroke="var(--icon-blue)" stroke-width="1"/>
        </svg>
        sleep@quorvana.com
      </li>
      <li class="contact-list__item">
        <svg class="contact-list__icon" viewBox="0 0 22 22" aria-hidden="true">
          <circle cx="11" cy="11" r="10" fill="var(--icon-blue)"/>
          <g fill="none" stroke="#fff" stroke-width="1">
            <circle cx="11" cy="11" r="5"/>
            <ellipse cx="11" cy="11" rx="2.2" ry="5"/>
            <path d="M6 11h10M6.8 8.5h8.4M6.8 13.5h8.4"/>
          </g>
        </svg>
        www.quorvana.com
      </li>
    </ul>
  </main>
</body>
</html>
```